Finish off design for Tool Retailer- One Page Brochure site

We have started work on our tool shop sit but need to to get finished. Just a One page WP that needs tidying up and made to look better and complete.
We also need to be able upload specials and monthly catalogs.
More info in the brief
Target Market(s)
Trades, mines, industiral
Coding
Coded - Design and coding required
Number of Pages Required
1 page
Font styles to use
Sans Serif
Requirements
Must have
- Please see brief
Nice to have
- Please see brief
Should not have
- Please see brief

```html
<!DOCTYPE html>
<html lang="en">
<head>
<meta charset="utf-8">
<title>Ridgeline Tools</title>
<link href="https://fonts.googleapis.com/css2?family=Lato:wght@400;700;900&family=Open+Sans:wght@400;600&display=swap" rel="stylesheet">
<style>
:root{
  --red:#b4001e;
  --red-dark:#7e0014;
  --black:#000;
  --ink:#1a1a1a;
  --grey-bg:#ebebeb;
  --card-border:#d4d4d4;
  --muted:#666;
  --star:#f2a024;
  --white:#fff;
}
*{box-sizing:border-box;margin:0;padding:0}
html,body{width:1200px;height:3309px;overflow:hidden}
body{position:relative;font-family:"Open Sans",Arial,sans-serif;color:var(--ink);background:var(--white)}
.abs{position:absolute}
h2,h3,.lato{font-family:"Lato",Arial,sans-serif}

/* header */
.topbar{left:0;top:0;width:1200px;height:113px;background:var(--red)}
.brand{left:161px;top:22px;width:240px;color:var(--white);font-family:"Lato",Arial,sans-serif;font-weight:900;line-height:1}
.brand .l1{font-size:24px;display:block;text-align:center}
.brand .l2{font-size:50px;display:block;text-align:center;letter-spacing:2px}
.newsletter{left:470px;top:44px;width:496px;height:44px;display:flex}
.newsletter .field{flex:1;background:var(--white);display:flex;align-items:center;padding-left:18px;font-size:14px;color:#999;gap:10px}
.newsletter .btn{width:110px;background:var(--black);color:var(--white);font-family:"Lato",Arial,sans-serif;font-weight:700;font-size:13px;display:flex;align-items:center;justify-content:center}
.account{left:930px;top:8px;color:var(--white);font-size:11px;font-family:"Lato",Arial,sans-serif;font-weight:700}
.mainnav{left:0;top:113px;width:1200px;height:68px;background:var(--black);display:flex;justify-content:center;align-items:center;gap:38px}
.mainnav a{color:var(--white);text-decoration:none;font-family:"Lato",Arial,sans-serif;font-weight:700;font-size:17px;display:flex;align-items:center;gap:7px}

/* hero */
.hero{left:0;top:181px;width:1200px;height:547px;background:linear-gradient(160deg,#a0001a 0%,#7d0014 48%,#5a5a5a 50%,#8c8c8c 75%,#4a4a4a 100%)}
.hero-title{left:0;top:240px;width:1200px;text-align:center;color:var(--white);font-family:"Lato",Arial,sans-serif;font-weight:900;font-size:48px;line-height:1}
.hero-sub{left:0;top:298px;width:1200px;text-align:center;color:var(--white);font-family:"Lato",Arial,sans-serif;font-weight:900;font-size:36px;line-height:1}
.hero-btn{left:518px;top:364px;width:168px;height:46px;border:2px solid var(--white);color:var(--white);font-family:"Lato",Arial,sans-serif;font-weight:700;font-size:16px;letter-spacing:2px;display:flex;align-items:center;justify-content:center}
.hero-product{left:353px;top:419px;width:507px;height:276px;background:radial-gradient(ellipse at center,#3a2a2c 0%,#2a1c1e 55%,rgba(40,30,30,0) 75%)}

/* sections */
.section-title{left:0;width:1200px;text-align:center;font-family:"Lato",Arial,sans-serif;font-weight:900;font-size:27px;color:var(--black)}
.section-title span{color:var(--red)}
.specials{left:0;top:728px;width:1200px;height:507px;background:var(--grey-bg)}
.card{background:var(--white);border:2px solid var(--card-border)}
.special-card{top:856px;width:210px;height:302px}
.special-card .photo{position:absolute;left:20px;top:20px;width:166px;height:150px;background:radial-gradient(circle,#c9c9c9 0%,#ececec 55%,#fff 75%)}
.special-card .name{position:absolute;left:22px;top:200px;font-family:"Lato",Arial,sans-serif;font-size:14px;font-weight:400}
.special-card .stars{position:absolute;left:22px;top:222px;display:flex;gap:1px}
.special-card .price{position:absolute;left:22px;top:254px;font-family:"Lato",Arial,sans-serif;font-size:20px;font-weight:700;color:var(--red)}
.special-card .more{position:absolute;left:106px;top:254px;width:88px;height:28px;background:var(--red);color:var(--white);font-size:10px;font-weight:600;display:flex;align-items:center;justify-content:center}

.catalogue-card{top:1341px;width:276px;height:329px}
.catalogue-card .photo{position:absolute;left:50px;top:20px;width:176px;height:180px;background:radial-gradient(circle,#c4c4c4 0%,#ececec 55%,#fff 75%)}
.catalogue-card .name{position:absolute;left:32px;top:228px;font-family:"Lato",Arial,sans-serif;font-weight:700;font-size:16px}
.catalogue-card .desc{position:absolute;left:32px;top:254px;width:220px;font-size:11.5px;line-height:21px;color:#444}

/* about */
.about-photo{left:480px;top:1736px;width:720px;height:461px;background:linear-gradient(180deg,#5f6f84 0%,#8a97a8 35%,#b7b1a6 60%,#3d3d3d 80%,#2b2b2b 100%)}
.about-panel{left:0;top:1736px}
.about-title{left:165px;top:1838px;color:var(--white);font-family:"Lato",Arial,sans-serif;font-weight:900;font-size:32px}
.about-text{left:165px;width:330px;color:var(--white);font-size:14.5px;line-height:22px}
.about-btn{left:170px;top:2069px;width:139px;height:40px;border:2px solid var(--white);color:var(--white);font-family:"Lato",Arial,sans-serif;font-weight:700;font-size:12px;display:flex;align-items:center;justify-content:center}

/* categories */
.categories{left:0;top:2197px;width:1200px;height:424px;background:var(--grey-bg)}
.category{top:2302px;width:252px;height:252px;border-radius:50%;border:2px solid var(--red);display:flex;align-items:center;justify-content:center}
.category .disc{width:230px;height:230px;border-radius:50%;background:var(--white);border:8px solid #cfcfcf;position:relative}
.category .photo{position:absolute;left:46px;top:28px;width:122px;height:100px;border-radius:10px;background:radial-gradient(circle,#bdbdbd 0%,#eaeaea 60%,#fff 80%)}
.category .label{position:absolute;left:0;width:214px;text-align:center;color:var(--red);font-family:"Lato",Arial,sans-serif;font-weight:700;font-size:16px;line-height:19px}

/* contact */
.contact-photo{left:0;top:2621px;width:593px;height:507px;background:linear-gradient(135deg,#2a2a2a 0%,#4a4a4a 45%,#3a3a3a 70%,#1f1f1f 100%)}
.form-title{left:139px;top:2684px;color:var(--white);font-family:"Lato",Arial,sans-serif;font-weight:700;font-size:24px}
.form-field{left:139px;width:390px;border-bottom:1px solid #8a8a8a;color:#c8c8c8;font-size:17px;padding-bottom:6px}
.send{left:148px;top:3002px;width:123px;height:38px;background:var(--red);color:var(--white);font-family:"Lato",Arial,sans-serif;font-weight:700;font-size:14px;display:flex;align-items:center;justify-content:center}
.info-title{left:655px;top:2684px;color:var(--red);font-family:"Lato",Arial,sans-serif;font-weight:900;font-size:26px}
.info-label{left:699px;color:var(--red);font-size:14px}
.info-value{left:699px;color:var(--ink);font-size:17px;line-height:29px}

/* footer */
.footer{left:0;top:3128px;width:1200px;height:181px;background:var(--black)}
.footer-nav{left:0;top:3168px;width:1200px;display:flex;justify-content:center;gap:24px}
.footer-nav a{color:var(--white);text-decoration:none;font-family:"Lato",Arial,sans-serif;font-weight:700;font-size:13px}
.copyright{left:0;top:3199px;width:1200px;text-align:center;color:#9a9a9a;font-size:12px}
.socials{left:521px;top:3238px;display:flex;gap:8px}
.socials span{width:34px;height:34px;border-radius:50%;border:2px solid var(--white)}
</style>
</head>
<body>

<!-- Header -->
<header class="abs topbar"></header>
<div class="abs brand"><span class="l1">Ridgeline</span><span class="l2">TOOLS</span></div>
<form class="abs newsletter">
  <div class="field">
    <svg width="18" height="14" viewBox="0 0 18 14"><rect x="1" y="1" width="16" height="12" fill="none" stroke="#999" stroke-width="1.5"/><path d="M1 1l8 7 8-7" fill="none" stroke="#999" stroke-width="1.5"/></svg>
    Email address
  </div>
  <div class="btn">SUBSCRIBE</div>
</form>
<div class="abs account">LOGIN &nbsp;|&nbsp; REGISTER</div>

<nav class="abs mainnav">
  <a href="#"><svg width="18" height="16" viewBox="0 0 18 16"><path d="M9 1L1 8h2.5v7h4v-5h3v5h4V8H17z" fill="#fff"/></svg>HOME</a>
  <a href="#"><svg width="18" height="18" viewBox="0 0 18 18"><circle cx="9" cy="9" r="8" fill="#fff"/><text x="9" y="13.5" text-anchor="middle" font-family="Lato,Arial,sans-serif" font-weight="900" font-size="12" fill="#000">?</text></svg>ABOUT US</a>
  <a href="#"><svg width="20" height="17" viewBox="0 0 20 17"><path d="M10 16S1 10 1 5a4.5 4.5 0 0 1 9-1 4.5 4.5 0 0 1 9 1c0 5-9 11-9 11z" fill="#fff"/></svg>SPECIALS</a>
  <a href="#"><svg width="16" height="16" viewBox="0 0 16 16"><path d="M3 1l3 3-2 2c1 2 4 5 6 6l2-2 3 3-2 2C7 14 2 9 1 3z" fill="#fff"/></svg>CONTACT US</a>
  <a href="#"><svg width="22" height="18" viewBox="0 0 22 18"><circle cx="8" cy="9" r="6" fill="none" stroke="#fff" stroke-width="3"/><circle cx="16" cy="6" r="4" fill="none" stroke="#fff" stroke-width="2.5"/></svg>CURRENT CATALOGUE</a>
</nav>

<!-- Hero -->
<section class="abs hero" role="img" aria-label="Red textured background sloping down to grey concrete"></section>
<div class="abs hero-product" role="img" aria-label="Set of red and black cordless power tools on battery packs"></div>
<h1 class="abs hero-title">ALL TOOS FOR ANY OCCASION</h1>
<div class="abs hero-sub">TOP QUALITY PRODUCTS</div>
<div class="abs hero-btn">VIEW MORE</div>
<svg class="abs" style="left:124px;top:398px" width="48" height="34" viewBox="0 0 48 34"><path d="M46 17H4M18 3L4 17l14 14" fill="none" stroke="#fff" stroke-width="4"/></svg>
<svg class="abs" style="left:1028px;top:398px" width="48" height="34" viewBox="0 0 48 34"><path d="M2 17h42M30 3l14 14-14 14" fill="none" stroke="#fff" stroke-width="4"/></svg>

<!-- Current specials -->
<section class="abs specials"></section>
<h2 class="abs section-title" style="top:781px">CURRENT <span>SPECIALS</span></h2>
<svg class="abs" style="left:102px;top:994px" width="40" height="24" viewBox="0 0 40 24"><path d="M38 12H3M13 2L3 12l10 10" fill="none" stroke="#888" stroke-width="2.5"/></svg>
<svg class="abs" style="left:1050px;top:994px" width="40" height="24" viewBox="0 0 40 24"><path d="M2 12h35M27 2l10 10-10 10" fill="none" stroke="#888" stroke-width="2.5"/></svg>

<article class="abs card special-card" style="left:161px">
  <div class="photo" role="img" aria-label="Orange corded drill"></div>
  <div class="name">PRODUCT TITLE</div>
  <div class="stars"><svg width="66" height="13" viewBox="0 0 66 13"><g fill="var(--star)"><path id="s" d="M6.5 0l2 4.2 4.5.6-3.3 3.1.8 4.6-4-2.2-4 2.2.8-4.6L0 4.8l4.5-.6z"/><use href="#s" x="13"/><use href="#s" x="26"/><use href="#s" x="39"/><use href="#s" x="52"/></g></svg></div>
  <div class="price">$99.50</div>
  <div class="more">MORE INFO</div>
</article>
<article class="abs card special-card" style="left:382px">
  <div class="photo" role="img" aria-label="Circular saw"></div>
  <div class="name">PRODUCT TITLE</div>
  <div class="stars"><svg width="66" height="13" viewBox="0 0 66 13"><g fill="var(--star)"><use href="#s"/><use href="#s" x="13"/><use href="#s" x="26"/><use href="#s" x="39"/><use href="#s" x="52"/></g></svg></div>
  <div class="price">$99.50</div>
  <div class="more">MORE INFO</div>
</article>
<article class="abs card special-card" style="left:604px">
  <div class="photo" role="img" aria-label="Yellow cordless drill kit with bag"></div>
  <div class="name">PRODUCT TITLE</div>
  <div class="stars"><svg width="66" height="13" viewBox="0 0 66 13"><g fill="var(--star)"><use href="#s"/><use href="#s" x="13"/><use href="#s" x="26"/><use href="#s" x="39"/><use href="#s" x="52"/></g></svg></div>
  <div class="price">$99.50</div>
  <div class="more">MORE INFO</div>
</article>
<article class="abs card special-card" style="left:825px">
  <div class="photo" role="img" aria-label="Compact cordless drill driver"></div>
  <div class="name" style="top:192px">PRODUCT TITLE</div>
  <div class="stars" style="top:214px"><svg width="66" height="13" viewBox="0 0 66 13"><g fill="var(--star)"><use href="#s"/><use href="#s" x="13"/><use href="#s" x="26"/><use href="#s" x="39"/><use href="#s" x="52"/></g></svg></div>
  <div class="price" style="top:244px">$99.50</div>
  <div class="more" style="top:244px">MORE INFO</div>
</article>

<!-- Latest catalogue -->
<h2 class="abs section-title" style="top:1277px">LATEST <span>CATALOGUE</span></h2>
<svg class="abs" style="left:102px;top:1503px" width="40" height="24" viewBox="0 0 40 24"><path d="M38 12H3M13 2L3 12l10 10" fill="none" stroke="#888" stroke-width="2.5"/></svg>
<svg class="abs" style="left:1050px;top:1503px" width="40" height="24" viewBox="0 0 40 24"><path d="M2 12h35M27 2l10 10-10 10" fill="none" stroke="#888" stroke-width="2.5"/></svg>

<article class="abs card catalogue-card" style="left:165px">
  <div class="photo" role="img" aria-label="Cordless nail gun"></div>
  <div class="name">PRODUCT TITLE</div>
  <p class="desc">Class aptent taciti sociosqu ad litora torquent per conubia nostra per</p>
</article>
<article class="abs card catalogue-card" style="left:461px">
  <div class="photo" role="img" aria-label="Lime green cordless tyre inflator"></div>
  <div class="name">PRODUCT TITLE</div>
  <p class="desc">Class aptent taciti sociosqu ad litora torquent per conubia nostra per</p>
</article>
<article class="abs card catalogue-card" style="left:761px">
  <div class="photo" role="img" aria-label="Cordless drill and impact driver combo kit"></div>
  <div class="name">PRODUCT TITLE</div>
  <p class="desc">Class aptent taciti sociosqu ad litora torquent per conubia nostra per</p>
</article>

<!-- About -->
<div class="abs about-photo" role="img" aria-label="Shopfront of the tool store with work utes parked outside"></div>
<svg class="abs about-panel" width="600" height="461" viewBox="0 0 600 461"><polygon points="0,0 496,0 600,232 490,461 0,461" fill="var(--red)"/></svg>
<h2 class="abs about-title">ABOUT US</h2>
<p class="abs about-text" style="top:1890px">Our Company started out with an idea to supply and meet the everyday tool needs of people.</p>
<p class="abs about-text" style="top:1952px">Maecenas aliquet velit vel turpis Mauris neque metus malesuada nec ultricies sit amet porttitor mattis enim In massa libero interdum nec interdum vel blandit sed</p>
<div class="abs about-btn">LEARN MORE</div>

<!-- Shop by category -->
<section class="abs categories"></section>
<h2 class="abs section-title" style="top:2236px;font-size:25px">SHOP BY CATEGORY</h2>
<svg class="abs" style="left:90px;top:2416px" width="40" height="24" viewBox="0 0 40 24"><path d="M38 12H3M13 2L3 12l10 10" fill="none" stroke="#888" stroke-width="2.5"/></svg>
<svg class="abs" style="left:1062px;top:2416px" width="40" height="24" viewBox="0 0 40 24"><path d="M2 12h35M27 2l10 10-10 10" fill="none" stroke="#888" stroke-width="2.5"/></svg>

<div class="abs category" style="left:150px"><div class="disc"><div class="photo" role="img" aria-label="Orange leaf blower"></div><div class="label" style="top:160px">Accessories</div></div></div>
<div class="abs category" style="left:362px"><div class="disc"><div class="photo" role="img" aria-label="Red air compressor"></div><div class="label" style="top:150px">Air Tools +<br>Compressors</div></div></div>
<div class="abs category" style="left:575px"><div class="disc"><div class="photo" role="img" aria-label="Green electric lawn mower"></div><div class="label" style="top:160px">Lawn Mowers</div></div></div>
<div class="abs category" style="left:787px"><div class="disc"><div class="photo" role="img" aria-label="Orange petrol lawn mower"></div><div class="label" style="top:154px">Hand Tools</div></div></div>

<!-- Contact -->
<div class="abs contact-photo" role="img" aria-label="Dark toned workshop with a tradesperson at a bench"></div>
<h2 class="abs form-title">CONTACT FORM</h2>
<div class="abs form-field" style="top:2741px">Name *</div>
<div class="abs form-field" style="top:2792px">E-mail *</div>
<div class="abs form-field" style="top:2854px">Phone Number *</div>
<div class="abs form-field" style="top:2906px;height:78px">Message</div>
<div class="abs send">SEND</div>

<h2 class="abs info-title">CONTACT US</h2>
<svg class="abs" style="left:654px;top:2760px" width="30" height="36" viewBox="0 0 30 36"><path d="M15 34S4 21 4 13a11 11 0 0 1 22 0c0 8-11 21-11 21z" fill="none" stroke="var(--red)" stroke-width="2"/><circle cx="15" cy="13" r="4" fill="none" stroke="var(--red)" stroke-width="2"/><ellipse cx="15" cy="34" rx="10" ry="2" fill="none" stroke="var(--red)" stroke-width="1.5"/></svg>
<div class="abs info-label" style="top:2754px">ADDRESS</div>
<div class="abs info-value" style="top:2778px">48 Quarry Road, Unit 5, Emerald Ridge</div>

<svg class="abs" style="left:654px;top:2848px" width="30" height="30" viewBox="0 0 30 30"><path d="M6 2l6 6-4 4c2 4 6 8 10 10l4-4 6 6-4 4C13 27 3 17 2 6z" fill="none" stroke="var(--red)" stroke-width="2" stroke-linejoin="round"/></svg>
<div class="abs info-label" style="top:2840px">PHONE NUMBER</div>
<div class="abs info-value" style="top:2864px">+61 400 555 017<br>+61 400 555 018</div>

<svg class="abs" style="left:654px;top:2964px" width="32" height="24" viewBox="0 0 32 24"><rect x="1" y="1" width="30" height="22" fill="none" stroke="var(--red)" stroke-width="2"/><path d="M1 1l15 12L31 1M1 23l11-10M31 23L20 13" fill="none" stroke="var(--red)" stroke-width="2"/></svg>
<div class="abs info-label" style="top:2954px">EMAIL ADDRESS</div>
<div class="abs info-value" style="top:2978px">hello@ridgelinetools.example</div>

<!-- Footer -->
<footer class="abs footer"></footer>
<nav class="abs footer-nav">
  <a href="#">HOME</a><a href="#">ABOUT US</a><a href="#">SPECIALS</a><a href="#">CONTACT US</a><a href="#">CURRENT CATALOGUE</a>
</nav>
<div class="abs copyright">Copyright © 2018 · Ridgeline Tools · All rights reserved</div>
<div class="abs socials"><span></span><span></span><span></span><span></span></div>

</body>
</html>
```